Vietnamese Restaurant Menu

We are an authentic Vietnamese noodle bar.

We would like our menu redesigned to become more attractive and have a picture for each item. We would like out new menu to look similar to the menu shown on the following website http://quantrelam.com.vn/?lang=en

Please find pictures and current menu attached.

If there are any items that you cannot find the pictures for please leave a space and we will add a picture into that slot.

```html
<!DOCTYPE html>
<html lang="en">
<head>
<meta charset="utf-8">
<title>Bamboo Lane – Menu</title>
<link rel="stylesheet" href="https://fonts.googleapis.com/css2?family=Fredoka:wght@400;600&display=swap">
<style>
:root{
  --bg:#ebebeb;
  --paper:#e4ddc2;
  --paper-edge:#d8d0b2;
  --frame:#5e4f45;
  --ink:#4a3f38;
  --brand:#8a6552;
  --gf-green:#6a9a3a;
  --gf-red:#c0502f;
  --food-warm:#c99a6b;
  --food-dark:#2f2a27;
}
*{box-sizing:border-box;margin:0;padding:0}
html,body{width:1109px;height:1200px;overflow:hidden;background:var(--bg)}
body{font-family:"Fredoka",sans-serif;color:var(--ink);position:relative}
.spread{position:absolute;left:24px;top:190px;width:1061px;height:820px;display:flex;gap:6px}
.page{position:relative;width:527px;height:820px;background:var(--paper);border:1px solid var(--paper-edge);overflow:hidden}
.frame{position:absolute;inset:10px;border:2px solid var(--frame);pointer-events:none}
.frame::before{content:"";position:absolute;inset:4px;border:1px solid var(--frame)}
.bamboo{position:absolute;opacity:.35;background:radial-gradient(ellipse at center,#a49a82 0%,rgba(164,154,130,0) 70%)}
.brand{position:absolute;left:0;right:0;top:24px;text-align:center}
.brand-name{display:inline-flex;align-items:center;gap:8px;font-size:34px;font-weight:600;color:var(--brand);line-height:1}
.brand-name .dot{width:14px;height:14px;border-radius:50%;background:var(--brand)}
.brand-tag{font-size:6.5px;font-weight:600;letter-spacing:.6px;color:var(--ink);margin-top:3px}
.section-title{position:absolute;left:16px;top:92px;font-size:12px;font-weight:600;letter-spacing:.3px}
.definition{position:absolute;left:16px;top:110px;width:480px;font-size:8.5px;line-height:1.45}
.note{position:absolute;left:16px;top:144px;font-size:10px;font-weight:600}
.gf{position:absolute;width:34px;height:34px;border-radius:50%;border:2px solid var(--gf-green);font-size:8px;line-height:1;color:var(--gf-red);display:flex;align-items:center;justify-content:center;text-align:center;background:#f0ead4}
.photo{position:absolute;border:1px solid #a89880}
.photo.rolls{background:radial-gradient(ellipse at 55% 60%,#d9a55a 0%,#8a6a3a 30%,var(--food-dark) 48%,#c9b9a6 70%)}
.photo.salad{background:radial-gradient(circle at 50% 50%,#c85a3a 0%,#7a4a30 28%,var(--food-dark) 45%,#d39a55 62%)}
.photo.greens{background:radial-gradient(circle at 50% 50%,#8fb36a 0%,#c9a27a 25%,var(--food-dark) 45%,#8a7a6a 62%)}
.photo.skewers{background:linear-gradient(90deg,#6a8a4a 0%,#4a3a2a 45%,#c0503a 70%,#3a3a30 100%)}
.photo.pho{background:radial-gradient(circle at 40% 50%,#7a9a5a 0%,#5a3a2a 22%,var(--food-dark) 40%,var(--food-warm) 60%)}
.photo.vegan{background:radial-gradient(circle at 40% 50%,#b0703a 0%,#6a8a4a 25%,var(--food-dark) 42%,#8c8c8c 62%)}
.item-name{position:absolute;font-size:7.5px;font-weight:600;text-align:center;letter-spacing:.3px;text-transform:uppercase;line-height:1.15}
.item-desc{position:absolute;font-size:7px;text-align:center;line-height:1.3}
.price{position:absolute;font-size:8px;text-align:center;line-height:1.35}
.main-price{position:absolute;font-size:8.5px;text-align:center;line-height:1.35}
.main-text{position:absolute;width:220px;font-size:7px;line-height:1.3}
.main-text h3{font-size:7.5px;font-weight:600;text-transform:uppercase;letter-spacing:.3px;margin-bottom:4px;line-height:1.2}
.main-text h4{font-size:7.5px;font-weight:600;margin-top:5px}
</style>
</head>
<body>
<div class="spread">

  <section class="page page-entrees">
    <div class="bamboo" style="left:130px;top:10px;width:260px;height:140px" role="img" aria-label="faint bamboo leaf decoration"></div>
    <div class="bamboo" style="left:10px;top:430px;width:300px;height:380px" role="img" aria-label="faint bamboo stalks and leaves decoration"></div>
    <div class="bamboo" style="left:340px;top:360px;width:180px;height:300px" role="img" aria-label="faint bamboo leaf decoration"></div>
    <div class="frame"></div>

    <header class="brand">
      <div class="brand-name"><span class="dot"></span>Bamboo Lane</div>
      <div class="brand-tag">PREMIUM VIETNAMESE NOODLE BAR</div>
    </header>

    <h2 class="section-title">MELODY OF ENTREES</h2>
    <p class="definition">/ˈmɛlədi/ a sequence of single notes that is musically satisfying in preparing your palate for an amazing epicurious experience</p>
    <p class="note">[all entrees are gluten free]</p>
    <div class="gf" style="left:205px;top:135px">Gluten<br>Free</div>

    <div class="photo rolls" style="left:16px;top:170px;width:138px;height:88px" role="img" aria-label="seafood spring rolls on a black plate"></div>
    <div class="item-name" style="left:16px;top:262px;width:138px">Seafood Spring Rolls</div>
    <div class="item-desc" style="left:16px;top:271px;width:138px">Shrimp, Crab, Taro, Mushroom, Water Chestnut</div>

    <div class="price" style="left:160px;top:210px;width:50px">(5pcs)<br>7.80</div>
    <div class="price" style="left:215px;top:210px;width:50px">(5pcs)<br>7.80</div>

    <div class="photo rolls" style="left:350px;top:170px;width:128px;height:58px" role="img" aria-label="vegetarian spring rolls on a black plate"></div>
    <div class="item-name" style="left:340px;top:262px;width:148px">Vegetarian Spring Rolls</div>
    <div class="item-desc" style="left:340px;top:271px;width:148px">Tofu, Taro, Mushroom, Onion</div>

    <div class="photo salad" style="left:16px;top:296px;width:138px;height:88px" role="img" aria-label="grilled chicken cabbage salad"></div>
    <div class="item-name" style="left:16px;top:388px;width:138px">Vietnamese Grilled Chicken Cabbage Salad</div>
    <div class="item-desc" style="left:16px;top:406px;width:138px">Cabbage, Carrots, Vietnamese Mint (Goi bap cai)</div>

    <div class="price" style="left:160px;top:338px;width:50px">8.80</div>
    <div class="price" style="left:215px;top:338px;width:50px">8.80</div>

    <div class="photo greens" style="left:350px;top:296px;width:128px;height:84px" role="img" aria-label="tofu mushroom cabbage salad"></div>
    <div class="item-name" style="left:340px;top:384px;width:148px">Vietnamese Tofu Mushroom Cabbage Salad</div>

    <div class="photo skewers" style="left:150px;top:415px;width:132px;height:88px" role="img" aria-label="street food skewers mixed plate"></div>
    <div class="item-name" style="left:140px;top:506px;width:152px">Vietnamese Street Food Skewers Mixed Plate</div>
    <div class="item-desc" style="left:130px;top:524px;width:172px">(Marinated Pork skewer + Nem Nuong skewer + Sugar Cane Prawn)</div>
    <div class="price" style="left:290px;top:446px;width:50px">8.80</div>
  </section>

  <section class="page page-mains">
    <div class="bamboo" style="left:20px;top:10px;width:500px;height:150px" role="img" aria-label="faint bamboo leaf decoration"></div>
    <div class="bamboo" style="left:10px;top:480px;width:510px;height:320px" role="img" aria-label="faint bamboo stalks and leaves decoration"></div>
    <div class="frame"></div>

    <header class="brand">
      <div class="brand-name"><span class="dot"></span>Bamboo Lane</div>
      <div class="brand-tag">PREMIUM VIETNAMESE NOODLE BAR</div>
    </header>

    <h2 class="section-title" style="top:100px">SYMPHONY OF MAINS</h2>
    <p class="definition" style="top:116px;width:370px">/ˈsɪmf(ə)ni/ an elaborate musical composition designed to fine-tune even the toughest of tastebuds</p>
    <p class="note" style="top:150px">[all mains are gluten free]</p>
    <div class="gf" style="left:145px;top:138px">Gluten<br>Free</div>

    <div class="photo pho" style="left:14px;top:175px;width:124px;height:84px" role="img" aria-label="bowl of beef noodle soup with chopsticks"></div>
    <div class="main-price" style="left:145px;top:190px;width:72px">medium 13.80<br>large 15.80</div>
    <div class="main-price" style="left:145px;top:222px;width:72px">Extra Beef Balls<br>4 pcs 2.00</div>
    <div class="main-text" style="left:225px;top:172px">
      <h3>12 Hour Vietnamese Beef Noodle Soup (Pho Bo)</h3>
      <p>Star Anise fruit, Clove buds, Fennel Seeds, Cardamom pods, Cinnamon quills simmered in a 12 hour beef bone marrow and oxtail broth</p>
      <h4>Choice of:</h4>
      <p>Plain and Simple: Rare Beef Tai<br>Adventurous: Rare Beef + Beef Flank Tai Nam<br>Safari: Rare Beef + Nam + Bo Vien Beef Balls + Tripe + Tendon (extra $1.50) Dac biet</p>
    </div>

    <div class="photo vegan" style="left:14px;top:294px;width:124px;height:82px" role="img" aria-label="bowl of vegan noodle soup with tomato and herbs"></div>
    <div class="main-price" style="left:145px;top:326px;width:72px">medium 13.80<br>large 15.80</div>
    <div class="main-text" style="left:225px;top:296px">
      <h3>6 Hour Vegan Vietnamese Noodle Soup (Pho Chay)</h3>
      <p>Star Anise fruit, Clove buds, Fennel Seeds, Cardamom pods, Cinnamon quills simmered in a 6 hour Onion, Pear, Carrot, Apple, Radish and Ginger broth</p>
    </div>

    <div class="photo pho" style="left:14px;top:415px;width:124px;height:84px" role="img" aria-label="bowl of chicken noodle soup with chopsticks"></div>
    <div class="main-price" style="left:145px;top:452px;width:72px">medium 13.80<br>large 15.80</div>
    <div class="main-text" style="left:225px;top:420px">
      <h3>8 Hour Vietnamese Chicken Noodle Soup (Pho Ga)</h3>
      <p>Star Anise fruit, Clove buds, Fennel Seeds, Cardamom pods, Cinnamon quills simmered in a 8 hour chicken bone broth</p>
    </div>
  </section>

</div>
</body>
</html>
```